Fielduro home page and search results web design

We are looking for an attractive front page and search page for our website, Fielduro.us. The site is currently up and can be searched. Most of the functionality works, but the design needs to be improved. The website is a platform that allows sports facility managers to list their facilities and allow the public to rent them. Can be thought of as the DineSlot for athletic facilities. The 2 pages we would like designed are the home page, where a renter would search for a facility, and the search results page, where there is a map of the facilities available on the left and the available facility listings on the right.

Target Market(s)

Sports facility managers and sports organizations

Number of Pages Required

2 page

Colors

Designer to choose colors to be used in the design.

Requirements
Must have
• Be very easy for someone visiting the site to use.

```html
<!DOCTYPE html>
<html lang="en">
<head>
<meta charset="utf-8">
<title>Fielduro – Facilities Management Portal</title>
<link href="https://fonts.googleapis.com/css2?family=Roboto:wght@300;400;500;700&display=swap" rel="stylesheet">
<style>
:root{
  --green:#7dc243;
  --green-dark:#6aad33;
  --ink:#333333;
  --muted:#666666;
  --light:#f4f5f7;
  --charcoal:#2b2b2b;
  --charcoal-2:#3a3a3a;
  --white:#ffffff;
  --line:#e3e3e3;
}
*{box-sizing:border-box;margin:0;padding:0}
html,body{width:1200px;height:2671px;overflow:hidden}
body{font-family:'Roboto',sans-serif;color:var(--ink);background:var(--white)}
.wrap{width:1030px;margin:0 auto;position:relative}

/* header */
.site-header{height:85px;border-top:4px solid var(--green);background:var(--white);position:relative}
.brand{position:absolute;left:85px;top:22px;display:flex;align-items:center;gap:10px;font-weight:700;font-size:32px;color:var(--ink);letter-spacing:-.5px}
.brand-dot{width:14px;height:14px;border-radius:50%;background:var(--green)}
.main-nav a{position:absolute;top:38px;font-size:12px;font-weight:500;color:#555;text-decoration:none;letter-spacing:.3px}

/* hero */
.hero{height:499px;position:relative;background:linear-gradient(180deg,#3f7d86 0%,#2c5d66 35%,#3d6b52 62%,#1c2b2c 100%);color:var(--white);text-align:center}
.hero-photo{position:absolute;inset:0;background:radial-gradient(ellipse at 55% 60%,rgba(140,190,120,.45),transparent 60%)}
.hero-content{position:relative;padding-top:118px}
.hero h1{font-size:34px;font-weight:500;letter-spacing:.5px}
.hero p{width:690px;margin:20px auto 0;font-size:14px;line-height:27px;font-weight:300}
.btn-green{display:inline-block;margin-top:18px;width:148px;height:48px;line-height:48px;background:var(--green);border:1px solid #9fd86f;color:var(--white);font-size:13px;font-weight:500}
.slider-dots{position:absolute;left:0;right:0;top:470px;display:flex;justify-content:center;gap:6px}
.slider-dots span{width:14px;height:14px;border-radius:50%;border:2px solid var(--white)}
.slider-dots span.active{background:var(--green)}

/* search */
.search-band{height:101px;background:var(--green);display:flex;align-items:center;padding-left:93px;gap:9px}
.search-band label{color:var(--white);font-size:18px;font-weight:500;margin-right:10px}
.search-band .field{width:192px;height:39px;background:var(--white);font-size:11px;color:#888;padding:12px 10px}
.btn-dark{background:var(--charcoal-2);color:var(--white);font-size:13px;font-weight:500;display:flex;align-items:center;justify-content:center;gap:14px}
.search-band .btn-dark{width:123px;height:39px;margin-left:0}

/* sections */
.section-title{text-align:center;font-size:22px;font-weight:500;color:var(--ink)}
.section-lead{text-align:center;font-size:12px;color:var(--muted);margin-top:14px}

.welcome{height:433px;padding-top:43px}
.features{display:grid;grid-template-columns:repeat(4,258px);margin-top:62px;text-align:center}
.feature-icon{width:107px;height:107px;border-radius:50%;margin:0 auto;border:4px solid var(--white);box-shadow:0 0 0 3px var(--green);display:flex;align-items:center;justify-content:center}
.feature-icon.green{background:var(--green)}
.feature-icon.dark{background:#555;box-shadow:0 0 0 3px #555}
.feature h3{font-size:15px;font-weight:500;margin-top:22px}
.feature p{font-size:12px;line-height:25px;color:var(--muted);margin-top:10px;padding:0 20px}

.featured{height:751px;background:var(--light);padding-top:50px}
.facility-grid{display:grid;grid-template-columns:repeat(4,246px);gap:14px;margin-top:28px}
.facility{background:var(--white);border:1px solid var(--line);height:278px}
.facility.wide{grid-column:span 2}
.facility-photo{height:196px}
.facility-photo.night{background:linear-gradient(180deg,#1a2540 0%,#3b4d7a 50%,#2f6a2a 100%)}
.facility-photo.stand{background:linear-gradient(180deg,#2a1f1c 0%,#7a5a3a 45%,#2f7a2d 100%)}
.facility-photo.day{background:linear-gradient(180deg,#8fb5d8 0%,#556a7a 55%,#3c8a34 100%)}
.facility-photo.clay{background:linear-gradient(180deg,#3e5a82 0%,#6a7d8c 55%,#c0663a 100%)}
.price{text-align:center;color:var(--green);font-size:18px;font-weight:500;margin-top:16px}
.place{text-align:center;color:var(--muted);font-size:12px;margin-top:10px}

.community{height:456px;padding-top:42px}
.video-grid{display:grid;grid-template-columns:repeat(3,333px);gap:15px;margin-top:33px}
.video{height:260px;position:relative;background:linear-gradient(180deg,#202020,#3a3a3a)}
.video.court{background:linear-gradient(180deg,#6f8f6a,#3d6a46)}
.video-play{position:absolute;left:50%;top:46%;transform:translate(-50%,-50%)}
.video-bar{position:absolute;left:0;right:0;bottom:0;height:28px;background:rgba(0,0,0,.75)}
.video-bar::before{content:"";position:absolute;left:0;right:0;top:0;height:4px;background:#555}
.video-caption{text-align:center;font-size:14px;color:var(--ink);margin-top:20px}

.newsletter{height:110px;background:var(--green);display:flex;align-items:center;padding-left:132px;gap:14px}
.newsletter label{color:var(--white);font-size:20px;font-weight:500;margin-right:0;width:290px}
.newsletter .field{width:486px;height:50px;background:var(--white)}
.newsletter .btn-dark{width:153px;height:50px;font-size:14px}

.site-footer{height:236px;background:var(--charcoal);padding-top:37px;color:var(--white)}
.social{display:flex;justify-content:center;gap:11px}
.social span{width:60px;height:60px;border-radius:50%;border:1px solid #8a8a8a;display:flex;align-items:center;justify-content:center}
.footer-rule{width:1030px;margin:17px auto 0;border-top:1px solid #444}
.footer-nav{display:flex;justify-content:center;gap:28px;font-size:12px;margin-top:24px}
.footer-nav i{font-style:normal;color:#aaa}
.copyright{text-align:center;font-size:11px;margin-top:30px;color:#ddd}
</style>
</head>
<body>

<header class="site-header">
  <div class="brand"><span>Fielduro</span><span class="brand-dot"></span></div>
  <nav class="main-nav">
    <a style="left:445px">HOME</a>
    <a style="left:542px">SEARCH</a>
    <a style="left:650px">RENTERS</a>
    <a style="left:761px">FACILITY MANAGER</a>
    <a style="left:933px">SUBSCRIPTION</a>
    <a style="left:1077px">LOGIN</a>
  </nav>
</header>

<section class="hero">
  <div class="hero-photo" role="img" aria-label="Floodlit stadium with a cheering crowd in silhouette"></div>
  <div class="hero-content">
    <h1>FACILITIES MANAGEMENT PORTAL</h1>
    <p>Manage your facilities, add facilities, available times, confirm bookings, track your earnings. View reports on your facilities usage, revenue generated by your</p>
    <span class="btn-green">LEARN MORE</span>
  </div>
  <div class="slider-dots"><span></span><span class="active"></span><span></span><span></span></div>
</section>

<section class="search-band">
  <label>SEARCH &amp; RESERVE FACILITIES :</label>
  <div class="field">City :</div>
  <div class="field">State :</div>
  <div class="field">Zipcode :</div>
  <div class="btn-dark">SEARCH
    <svg width="12" height="12" viewBox="0 0 12 12"><circle cx="5" cy="5" r="3.6" fill="none" stroke="#fff" stroke-width="1.6"/><line x1="7.6" y1="7.6" x2="11" y2="11" stroke="#fff" stroke-width="1.8"/></svg>
  </div>
</section>

<section class="welcome">
  <div class="wrap">
    <h2 class="section-title">WELCOME TO FIELDURO</h2>
    <p class="section-lead">Fielduro is an online platform and marketplace for people to list, discover, and book facilities for sports activities.</p>
    <div class="features">
      <div class="feature">
        <div class="feature-icon green"><svg width="44" height="50" viewBox="0 0 44 50"><path d="M22 4a14 14 0 0 0-8 25.5V36h16v-6.5A14 14 0 0 0 22 4z" fill="none" stroke="#fff" stroke-width="3"/><line x1="15" y1="42" x2="29" y2="42" stroke="#fff" stroke-width="3"/></svg></div>
        <h3>HOW IT WORKS</h3>
        <p>Fielduro is an online platform &amp; market place for people to list, discover, &amp;book facilities for sports activities.</p>
      </div>
      <div class="feature">
        <div class="feature-icon dark"><svg width="56" height="36" viewBox="0 0 56 36"><path d="M4 10l10-6 10 4 8-4 10 2 10 6-6 12-12 8-10-6-14-4z" fill="#fff"/></svg></div>
        <h3>RENTERS</h3>
        <p>Fielduro is an online platform &amp; market place for people to list, discover, &amp;book facilities for sports activities.</p>
      </div>
      <div class="feature">
        <div class="feature-icon green"><svg width="40" height="44" viewBox="0 0 40 44"><circle cx="20" cy="12" r="9" fill="#fff"/><path d="M2 42c0-12 8-18 18-18s18 6 18 18z" fill="#fff"/></svg></div>
        <h3>OWNERS</h3>
        <p>Fielduro is an online platform &amp; market place for people to list, discover, &amp;book facilities for sports activities.</p>
      </div>
      <div class="feature">
        <div class="feature-icon dark"><svg width="36" height="46" viewBox="0 0 36 46"><rect x="3" y="6" width="30" height="38" rx="2" fill="none" stroke="#fff" stroke-width="3"/><rect x="11" y="2" width="14" height="8" fill="#fff"/><g stroke="#fff" stroke-width="2.5"><line x1="9" y1="19" x2="27" y2="19"/><line x1="9" y1="27" x2="27" y2="27"/><line x1="9" y1="35" x2="27" y2="35"/></g></svg></div>
        <h3>BENEFITS</h3>
        <p>Fielduro is an online platform &amp; market place for people to list, discover, &amp;book facilities for sports activities.</p>
      </div>
    </div>
  </div>
</section>

<section class="featured">
  <div class="wrap">
    <h2 class="section-title">FEATURED FACILITIES</h2>
    <p class="section-lead">Fielduro is an online platform and marketplace for people to list, discover, and book facilities for sports activities.</p>
    <div class="facility-grid">
      <div class="facility wide"><div class="facility-photo stand" role="img" aria-label="Stadium under floodlights at night"></div><div class="price">$50 PER HOUR</div><div class="place">Indoor Soccer Field Dallas, TX, 75028</div></div>
      <div class="facility"><div class="facility-photo night" role="img" aria-label="Empty arena lit by spotlights"></div><div class="price">$80 PER HOUR</div><div class="place">Indoor Soccer Field Dallas, TX, 75028</div></div>
      <div class="facility"><div class="facility-photo clay" role="img" aria-label="Baseball diamond with clay infield"></div><div class="price">$20 PER HOUR</div><div class="place">Indoor Basketball Field Dallas, TX, 75028</div></div>
      <div class="facility"><div class="facility-photo night" role="img" aria-label="Green pitch under bright stadium lights"></div><div class="price">$60 PER HOUR</div><div class="place">Baseball Field Dallas, TX, 75028</div></div>
      <div class="facility"><div class="facility-photo night" role="img" aria-label="Striped pitch under spotlights"></div><div class="price">$80 PER HOUR</div><div class="place">Baseball Field Dallas, TX, 75028</div></div>
      <div class="facility wide"><div class="facility-photo day" role="img" aria-label="Open stadium with full stands in daylight"></div><div class="price">$56 PER HOUR</div><div class="place">Baseball Field Dallas, TX, 75028</div></div>
    </div>
  </div>
</section>

<section class="community">
  <div class="wrap">
    <h2 class="section-title">MEET OUR COMMUNITY</h2>
    <p class="section-lead" style="margin-top:10px">See what people are saying about Fielduro</p>
    <div class="video-grid">
      <div>
        <div class="video court" role="img" aria-label="Video testimonial of a facility manager on a tennis court">
          <svg class="video-play" width="56" height="40" viewBox="0 0 56 40"><rect width="56" height="40" rx="10" fill="#555"/><path d="M22 12l14 8-14 8z" fill="#fff"/></svg>
          <div class="video-bar"></div>
        </div>
        <div class="video-caption">Facility Manager - Ryan Mercer</div>
      </div>
      <div>
        <div class="video" role="img" aria-label="Video testimonial of a renter in a basketball jersey">
          <svg class="video-play" width="56" height="40" viewBox="0 0 56 40"><rect width="56" height="40" rx="10" fill="#555"/><path d="M22 12l14 8-14 8z" fill="#fff"/></svg>
          <div class="video-bar"></div>
        </div>
        <div class="video-caption">Renter - Leo Danton</div>
      </div>
      <div>
        <div class="video" role="img" aria-label="Video testimonial of a facility owner in a team jersey">
          <svg class="video-play" width="56" height="40" viewBox="0 0 56 40"><rect width="56" height="40" rx="10" fill="#555"/><path d="M22 12l14 8-14 8z" fill="#fff"/></svg>
          <div class="video-bar"></div>
        </div>
        <div class="video-caption">Facility Owner - Owen Halley</div>
      </div>
    </div>
  </div>
</section>

<section class="newsletter">
  <label>NEWSLETTER SUBSCRIPTION :</label>
  <div class="field"></div>
  <div class="btn-dark">SUBSCRIBE</div>
</section>

<footer class="site-footer">
  <div class="social">
    <span></span><span></span><span></span><span></span><span></span>
    <span><svg width="18" height="14" viewBox="0 0 18 14"><rect x="1" y="1" width="16" height="12" rx="1.5" fill="none" stroke="#fff" stroke-width="1.5"/><path d="M1.5 2l7.5 6 7.5-6" fill="none" stroke="#fff" stroke-width="1.5"/></svg></span>
  </div>
  <div class="footer-rule"></div>
  <nav class="footer-nav">
    <span>HOME</span><i>|</i><span>SEARCH</span><i>|</i><span>RENTERS</span><i>|</i><span>FACILITY MANAGER</span><i>|</i><span>SUBSCRIPTION</span><i>|</i><span>LOGIN</span>
  </nav>
  <p class="copyright">© Copyrights 2017 Fielduro.All Rights Reserved.</p>
</footer>

</body>
</html>
```